Recruitment website for new startup company - Tal Brisk Recruitment

Hi , I need to design a web page for my new recruitment company with the ability to link to social media accounts. The ability to add and remove job posts along with a blog page which I can update. More importantly I need the website to have the functionality of applicants being able to upload their cv and somewhere for me to store it. I will need assistance/recommendation for email address with company name, hosting and security. An about us page. The website will also need a search function for applicants to narrow down the search. Again I will need to be able to update this myself as the company grows. I have my logo ready domain address ready and would like the web site done ASAP. Thank you for your help.
Updates

Project Deadline Extended
Reason: Want to get a few more ideas and variations to designs done. But using logo as inspiration Thanks

Target Market(s)

Financial and property industry so professionals. New starters to senior management age range 25-60

Industry/Entity Type

Financial

Coding

Coded - Design and coding required

Number of Pages Required

4 page

Colors

Designer to choose colors to be used in the design.

Requirements
Must have
• Ability for me to add amend and remove job posts, ability for applicants to upload cv and for me to store and access it. Link to social media accounts
Should not have
• Needs to be clean approachable so not to childish but must come across as approachable and trustworthy.
• No yellow please my logo has a gold V not yellow. If it looks yellow use a different colour please. Thanks

```html
<!DOCTYPE html>
<html lang="en">
<head>
<meta charset="utf-8">
<title>Tal Brisk Recruitment</title>
<link href="https://fonts.googleapis.com/css2?family=Poppins:wght@300;400;500;600;700&display=swap" rel="stylesheet">
<style>
:root{
  --navy:#1f3a66;
  --navy-dark:#17305a;
  --gold:#c6a54b;
  --gold-soft:#d4b967;
  --ink:#333;
  --muted:#777;
  --line:#d9d9d9;
  --footer:#1e1e1e;
  --footer-line:#333;
  --white:#fff;
}
*{box-sizing:border-box;margin:0;padding:0}
html,body{width:1200px;height:3779px;overflow:hidden}
body{font-family:'Poppins',sans-serif;color:var(--ink);background:var(--white);position:relative}
.abs{position:absolute}
/* top bar */
.topbar{left:0;top:0;width:1200px;height:36px;background:var(--navy);color:#fff;font-size:13px}
.topbar .mail{right:228px;top:9px}
.topbar .sep{right:210px;top:8px;width:1px;height:20px;background:#fff}
.topbar .soc{top:12px;width:12px;height:12px;border-radius:50%;background:#fff}
/* header */
.header{left:0;top:36px;width:1200px;height:77px;background:#fff;border-bottom:1px solid #eee}
.brand{left:62px;top:20px;font-weight:600;color:var(--navy);font-size:17px;line-height:19px;letter-spacing:1px}
.nav{left:245px;top:30px;display:flex;gap:28px;font-size:13px;color:var(--navy)}
.nav .active{color:var(--navy);font-weight:600}
.login{left:762px;top:30px;font-size:13px;color:var(--navy)}
.cv-btn{left:996px;top:14px;width:190px;height:44px;border:2px solid var(--gold);border-radius:22px;background:var(--gold);color:#fff;font-weight:600;font-size:17px;display:flex;align-items:center;justify-content:center}
/* hero */
.hero{left:0;top:113px;width:1200px;height:517px;background:linear-gradient(135deg,#2d4a74 0%,#4d6d95 45%,#27416a 100%)}
.hero-title{left:0;top:178px;width:1200px;text-align:center;color:#fff;font-size:38px;font-weight:700}
.hero-sub{left:0;top:224px;width:1200px;text-align:center;color:#fff;font-size:14px}
.search{left:227px;top:265px;width:743px;height:50px;background:#fff;border-radius:25px;display:flex;align-items:center;font-size:14px;color:var(--muted)}
.search .f{display:flex;align-items:center;gap:8px;height:30px;padding-left:28px}
.search .f.kw{width:270px;border-right:1px solid var(--line)}
.search .f.loc{width:150px;border-right:1px solid var(--line)}
.search .f.sec{width:170px}
.search .go{margin-left:auto;margin-right:8px;width:124px;height:36px;border-radius:18px;background:var(--gold);color:#fff;font-weight:600;display:flex;align-items:center;justify-content:center;gap:8px}
.browse{left:0;top:337px;width:1200px;text-align:center;color:#fff;font-size:13px}
.browse span{color:var(--gold-soft)}
/* steps */
.h2{font-size:33px;font-weight:700;color:var(--navy);text-align:center}
.steps-title{left:0;top:695px;width:1200px}
.steps-title u{color:var(--gold);text-decoration-thickness:3px}
.steps-sub{left:0;top:758px;width:1200px;text-align:center;color:var(--muted);font-size:17px}
.track{left:252px;top:916px;width:706px;height:12px;background:var(--gold)}
.step{top:852px;width:140px;height:140px;border-radius:50%;background:var(--gold);display:flex;align-items:center;justify-content:center}
.step .in{width:112px;height:112px;border-radius:50%;background:var(--navy);display:flex;align-items:center;justify-content:center}
.step-label{top:995px;width:200px;text-align:center;font-size:20px;color:var(--navy)}
/* jobs */
.sec-h{font-size:28px;font-weight:700;color:#222}
.pager{top:1143px;width:28px;height:30px;display:flex;align-items:center;justify-content:center}
.jobs{left:156px;top:1192px;width:582px}
.job{height:111px;border:2px solid var(--line);margin-bottom:0;position:relative;padding:26px 0 0 30px;background:#fff}
.job + .job{border-top:none}
.job.hl{background:#d7d7d7}
.job.last{margin-top:16px;border-top:2px solid var(--line)}
.job h3{font-size:21px;font-weight:400;color:var(--navy)}
.job .meta{font-size:13px;color:var(--muted);margin-top:10px;display:flex;gap:28px}
.tag{position:absolute;right:20px;top:26px;background:var(--gold);color:#fff;font-size:12px;font-weight:600;padding:3px 11px;border-radius:6px}
.posted{position:absolute;right:20px;top:68px;font-size:13px;color:var(--muted)}
.featured{left:761px;top:1192px;width:280px;height:559px;border:2px solid var(--line)}
.featured .photo{margin:0;height:236px;background:linear-gradient(160deg,#e9eef3,#a9b8c9 60%,#7f93a9)}
.featured .body{padding:24px 22px}
.featured h3{font-size:20px;font-weight:700;color:var(--navy);line-height:28px}
.featured .tag{position:static;display:inline-block;margin-top:12px;font-size:11px}
.featured .meta{font-size:13px;color:var(--navy);margin-top:12px;display:flex;gap:16px}
.featured p{font-size:12px;color:var(--muted);margin-top:8px;line-height:20px}
.apply{margin:22px auto 0;width:170px;height:36px;border-radius:18px;background:var(--navy);color:#fff;font-size:13px;font-weight:600;display:flex;align-items:center;justify-content:center}
.dots{display:flex;gap:8px;justify-content:center;margin-top:22px}
.dots i{width:7px;height:7px;border-radius:50%;background:#ccc}
.dots i:first-child{background:var(--gold)}
.pill{height:42px;border:2px solid var(--navy);border-radius:21px;color:var(--navy);font-weight:600;font-size:15px;display:flex;align-items:center;justify-content:center;gap:8px;background:#fff}
/* bands */
.resume-band{left:0;top:1971px;width:1200px;height:70px;background:var(--gold);color:#fff;font-size:21px}
.resume-band .txt{left:230px;top:20px}
.resume-band .btn{left:808px;top:15px;width:160px;height:40px;border:2px solid #fff;border-radius:20px;font-size:13px;font-weight:600;display:flex;align-items:center;justify-content:center}
.refer{left:0;top:2041px;width:1200px;height:504px;background:linear-gradient(120deg,#4a4f57 0%,#7b7f84 40%,#5d5b56 70%,#3e3c3a 100%)}
.refer-title{left:0;top:2210px;width:1200px;text-align:center;color:#fff;font-size:38px;font-weight:700;line-height:52px}
.refer-sub{left:0;top:2318px;width:1200px;text-align:center;color:#fff;font-size:16px;line-height:30px}
.refer-btn{left:543px;top:2393px;width:170px;height:44px;border:2px solid var(--gold);border-radius:22px;color:var(--gold);font-size:14px;font-weight:600;display:flex;align-items:center;justify-content:center}
/* blog */
.blog-title{left:0;top:2600px;width:1200px}
.blog-title span{color:var(--gold)}
.blog-sub{left:250px;top:2660px;width:700px;text-align:center;color:var(--muted);font-size:14px;line-height:32px}
.post-img{top:2764px;width:466px;height:210px}
.post-date{top:3000px;width:70px;text-align:right;color:var(--navy);font-weight:700;font-size:19px;line-height:30px}
.post-bar{top:3002px;width:3px;height:62px;background:var(--gold)}
.post-text{top:3002px;width:340px;font-size:13px;color:var(--muted);line-height:30px}
/* footer */
.footer{left:0;top:3233px;width:1200px;height:546px;background:var(--footer);color:#bbb}
.f-h{font-size:17px;font-weight:600;color:var(--gold)}
.f-h.w{color:#fff}
.news-input{left:143px;top:3345px;width:213px;height:38px;background:#fff;font-size:13px;color:#999;padding:10px 12px}
.news-btn{left:356px;top:3345px;width:124px;height:38px;background:var(--gold);color:#fff;font-size:13px;font-weight:600;display:flex;align-items:center;justify-content:center;gap:6px}
.f-soc{top:3346px;width:32px;height:32px;border-radius:50%;border:2px solid var(--gold);background:transparent}
.call{left:819px;top:3349px;color:#fff;font-size:14px}
.call b{font-size:22px;font-weight:700;margin-left:6px}
.f-brand{left:143px;top:3468px;font-size:22px;font-weight:600;color:#9a9a9a;letter-spacing:2px;line-height:28px}
.f-about{left:143px;top:3550px;width:210px;font-size:13px;line-height:30px;color:#ddd}
.f-list{list-style:none;font-size:14px;line-height:32px;color:#ddd}
.f-list li::before{content:"";display:inline-block;border-left:6px solid #ddd;border-top:4px solid transparent;border-bottom:4px solid transparent;margin-right:10px}
.f-list li.on{color:var(--gold)}
.f-list li.on::before{border-left-color:var(--gold)}
.field{left:822px;width:236px;background:#e8e8e8;font-size:12px;color:#999;padding:8px 10px}
.send{left:1010px;top:3591px;width:48px;height:62px;background:var(--gold);display:flex;align-items:center;justify-content:center}
.f-rule{left:143px;top:3694px;width:915px;height:1px;background:var(--footer-line)}
.copy{left:0;top:3712px;width:1200px;text-align:center;font-size:12px;color:#ddd}
</style>
</head>
<body>

<div class="abs topbar">
  <span class="abs mail">&#9993; info@talbriskrecruitment.com</span>
  <span class="abs sep"></span>
  <span class="abs soc" style="right:180px"></span>
  <span class="abs soc" style="right:140px"></span>
  <span class="abs soc" style="right:100px"></span>
  <span class="abs soc" style="right:60px"></span>
</div>

<header class="abs header">
  <div class="abs brand">TAL BRISK<br>RECRUITMENT</div>
  <nav class="abs nav"><span class="active">HOME</span><span>ABOUT</span><span>RECRUITMENT</span><span>NEWS</span><span>CONTACT</span></nav>
  <div class="abs login">LOGIN / REGISTER
    <svg width="22" height="18" viewBox="0 0 22 18" style="vertical-align:middle;margin-left:10px"><rect x="8" y="1" width="12" height="16" fill="none" stroke="#1f3a66" stroke-width="1.5"/><path d="M1 9h11M8 5l4 4-4 4" fill="none" stroke="#1f3a66" stroke-width="1.5"/></svg>
  </div>
  <div class="abs cv-btn">CV Drop Point</div>
</header>

<section class="abs hero" role="img" aria-label="Photo of business people shaking hands across a meeting table"></section>
<h1 class="abs hero-title">Multi-Industry Recruitment Agency</h1>
<p class="abs hero-sub">Select your sector and/or type job keywords, then click search to find your perfect job.</p>
<div class="abs search">
  <div class="f kw"><svg width="14" height="14" viewBox="0 0 14 14"><circle cx="6" cy="6" r="4.5" fill="none" stroke="#777" stroke-width="1.6"/><path d="M9.5 9.5L13 13" stroke="#777" stroke-width="1.6"/></svg>Job Keywords</div>
  <div class="f loc"><svg width="10" height="14" viewBox="0 0 10 14"><path d="M5 13C2 9 1 7 1 5a4 4 0 018 0c0 2-1 4-4 8z" fill="none" stroke="#777" stroke-width="1.3"/></svg>Location &nbsp;&#8964;</div>
  <div class="f sec"><svg width="12" height="13" viewBox="0 0 12 13"><circle cx="6" cy="4" r="3" fill="#777"/><path d="M0 13c0-4 3-5 6-5s6 1 6 5z" fill="#777"/></svg>Sector &nbsp;&nbsp;&#8964;</div>
  <div class="go"><svg width="13" height="13" viewBox="0 0 14 14"><circle cx="6" cy="6" r="4.5" fill="none" stroke="#fff" stroke-width="1.8"/><path d="M9.5 9.5L13 13" stroke="#fff" stroke-width="1.8"/></svg>Search</div>
</div>
<p class="abs browse">or browse job offers by <span>category</span></p>

<h2 class="abs h2 steps-title">All the jobs you want in <u>one</u> simple place.</h2>
<p class="abs steps-sub">Find the jobs you want in just a few simple quicks.</p>
<div class="abs track"></div>
<div class="abs step" style="left:182px"><div class="in"><svg width="46" height="46" viewBox="0 0 46 46"><circle cx="23" cy="23" r="22" fill="#fff"/><circle cx="21" cy="20" r="8" fill="none" stroke="#1f3a66" stroke-width="4"/><path d="M27 26l7 7" stroke="#1f3a66" stroke-width="5" stroke-linecap="round"/></svg></div></div>
<div class="abs step" style="left:547px"><div class="in"><svg width="50" height="50" viewBox="0 0 50 50"><rect x="6" y="8" width="34" height="36" rx="3" fill="none" stroke="#fff" stroke-width="3"/><path d="M18 34l4-10 18-18 6 6-18 18z" fill="none" stroke="#fff" stroke-width="3"/></svg></div></div>
<div class="abs step" style="left:888px"><div class="in"><svg width="50" height="54" viewBox="0 0 50 54"><circle cx="25" cy="16" r="11" fill="none" stroke="#fff" stroke-width="3"/><path d="M5 52c0-14 9-22 20-22s20 8 20 22z" fill="none" stroke="#fff" stroke-width="3"/><path d="M25 32l-4 6 4 12 4-12z" fill="#fff"/></svg></div></div>
<div class="abs step-label" style="left:152px">SEARCH</div>
<div class="abs step-label" style="left:517px">APPLY</div>
<div class="abs step-label" style="left:858px">HIRED</div>

<h2 class="abs sec-h" style="left:156px;top:1140px">Recent Jobs</h2>
<div class="abs pager" style="left:674px;color:#999">&lsaquo;</div>
<div class="abs pager" style="left:704px;background:var(--gold);color:#fff">&rsaquo;</div>
<h2 class="abs sec-h" style="left:761px;top:1140px">Featured Jobs</h2>

<div class="abs jobs">
  <div class="job"><h3>Sales &amp; Marketing Coordinator</h3><div class="meta"><span>&#9906; Germany, Hannover</span><span>&#9432; £27,500</span></div><span class="tag">Full Time</span><span class="posted">Posted 12 hours ago</span></div>
  <div class="job"><h3>Engineering Technician</h3><div class="meta"><span>&#9906; Netherlands, Rotterdam</span><span>&#9432; £27,000 – £30,000</span></div><span class="tag">Full Time</span><span class="posted">Posted 15 hours ago</span></div>
  <div class="job hl"><h3>Science Teacher</h3><div class="meta"><span>&#9906; England, London, Camden</span><span>&#9432; £30,000 – £32,500</span></div><span class="tag">Full Time</span><span class="posted">Posted 2 days ago</span></div>
  <div class="job"><h3>Accounts Assistant</h3><div class="meta"><span>&#9906; England, Hampshire, Gosport</span><span>&#9432; £31,900 – £36,970</span></div><span class="tag">Full Time</span><span class="posted">Posted 12 days ago</span></div>
  <div class="job last"><h3>Clinical Support Specialist</h3><div class="meta"><span>&#9906; Madrid, Spain</span><span>&#9432; £12,900 – £18,970</span></div><span class="tag">Part Time</span><span class="posted">Posted 16 hours ago</span></div>
</div>

<aside class="abs featured">
  <div class="photo" role="img" aria-label="Photo of a desk with financial charts, a pen and glasses"></div>
  <div class="body">
    <h3>Account Fraud Prevention Officer</h3>
    <span class="tag">Full Time</span>
    <div class="meta"><span>&#9906; Germany, Hannover</span><span style="color:#777">&#9432; £27,500</span></div>
    <p>Lorem ipsum dolor sit amet, consectetur adipiscing elit. Nunc a congue magna, non maximus eros. Aliquam erat volutpat. Donec suscipit id ante in pulvinar.</p>
    <div class="apply">Apply for this Job</div>
    <div class="dots"><i></i><i></i><i></i></div>
  </div>
</aside>

<div class="abs pill" style="left:366px;top:1783px;width:176px">View all Jobs &rsaquo;</div>

<div class="abs resume-band">
  <span class="abs txt">Add your resume and let your next job find you.</span>
  <span class="abs btn">ADD RESUME</span>
</div>
<section class="abs refer" role="img" aria-label="Photo of a smiling man working at a laptop in an office"></section>
<h2 class="abs refer-title">Refer a friend and get £250 on<br>successful placement</h2>
<p class="abs refer-sub">In enim justo, rhoncus ut, imperdiet a, venenatis vitae, justo.<br>Nullam dictum felis eu pede mollis pretium.</p>
<div class="abs refer-btn">REFER A FRIEND</div>

<h2 class="abs h2 blog-title">Latest Blogs from<span>TAL BRISK</span></h2>
<p class="abs blog-sub">In enim justo, rhoncus ut, imperdiet a, venenatis vitae, justo. Nullam dictum felis eu pede mollis pretium. Integer tincidunt. Cras dapibus. Vivamus elementum semper nisi. Aenean vulputate eleifend tellus.</p>

<div class="abs post-img" style="left:121px;background:linear-gradient(150deg,#eef1f4,#b8c3cf 55%,#8795a5)" role="img" aria-label="Photo of hands reviewing documents and a tablet on a white desk"></div>
<div class="abs post-img" style="left:612px;background:linear-gradient(150deg,#f1ede6,#c9bba5 55%,#8f8a86)" role="img" aria-label="Photo of a smiling office team gathered around a laptop"></div>

<div class="abs post-date" style="left:131px">Nov 01,<br>2017</div>
<div class="abs post-bar" style="left:217px"></div>
<p class="abs post-text" style="left:232px">Etiam ultricies nisi vel augue. Curabitur ullamcorper ultricies tellus eget condimentum nisi.</p>
<div class="abs post-date" style="left:618px">Oct 11,<br>2017</div>
<div class="abs post-bar" style="left:704px"></div>
<p class="abs post-text" style="left:719px">Etiam ultricies nisi vel augue. Curabitur ullamcorper ultricies tellus eget condimentum nisi.</p>

<div class="abs pill" style="left:506px;top:3099px;width:182px">Read all News &rsaquo;</div>
<div class="abs pager" style="left:1012px;top:3104px;color:#999">&lsaquo;</div>
<div class="abs pager" style="left:1040px;top:3104px;background:var(--gold);color:#fff">&rsaquo;</div>

<footer class="abs footer"></footer>
<div class="abs f-h" style="left:143px;top:3310px">Subscribe to our Newsletter</div>
<div class="abs news-input">Your email address</div>
<div class="abs news-btn"><svg width="14" height="12" viewBox="0 0 14 12"><path d="M0 5L14 0 10 12 7 7z" fill="#fff"/></svg>SUBSCRIBE</div>
<div class="abs f-h" style="left:562px;top:3310px">Follow us on</div>
<span class="abs f-soc" style="left:562px"></span>
<span class="abs f-soc" style="left:610px"></span>
<span class="abs f-soc" style="left:656px"></span>
<span class="abs f-soc" style="left:704px"></span>
<div class="abs f-h" style="left:819px;top:3306px">Need Help?</div>
<div class="abs call">&#9990; CALL US: <b>1800-555-0199</b></div>

<div class="abs f-brand">TAL BRISK<br>RECRUITMENT</div>
<p class="abs f-about">Lorem ipsum dolor sit amet, consectetur adipiscing elit. Cras orci sem, vulputate sit amet ipsum vel en el.</p>

<div class="abs f-h w" style="left:408px;top:3456px">Information</div>
<ul class="abs f-list" style="left:408px;top:3490px"><li>About Us</li><li class="on">Help Desk</li><li>Support</li><li>Privacy Policy</li><li>Terms &amp; Conditions</li></ul>
<div class="abs f-h w" style="left:612px;top:3456px">Useful Links</div>
<ul class="abs f-list" style="left:612px;top:3490px"><li>Home</li><li>Search Job</li><li>Positions</li><li>Latest News</li><li class="on">Jobs</li></ul>
<div class="abs f-h w" style="left:822px;top:3456px">Get in Touch</div>
<div class="abs field" style="top:3494px;height:34px">Name</div>
<div class="abs field" style="top:3540px;height:34px">Email address</div>
<div class="abs field" style="top:3591px;height:62px;width:188px">Message</div>
<div class="abs send"><svg width="18" height="16" viewBox="0 0 14 12"><path d="M0 5L14 0 10 12 7 7z" fill="#fff"/></svg></div>
<div class="abs f-rule"></div>
<p class="abs copy">TAL BRISK Copyright © 2017. All rights reserved.</p>

</body>
</html>
```